Swimming Pool Service Website needed!!!

Hi Everyone! Thanks for looking at my contest. I PROMISE to provide excellent feedback during this process.

I am starting a new swimming pool business cleaning company in San Diego, California and would like your help in making it similar to one of these two websites that are already functioning.

http://www.brightlagoonworks.example/services-repair.html

http://tidemarkaquacare.example/commercial-pool-cleaning.php

I like these two because they are easy to read, classy, sophisticated and have nice pictures of really clean & clear pools.

I really like the blue on white color format.

I do not have a logo, but the name of my company is GLIMMERWAVE POOL SERVICE.

My tag line is: Water so pure, it sparkles like a summer sky. (does not need to have the quotes around "in"...maybe just italics for this word IN?) You decide for me.

I would like to have a logo designed that incorporates some sort of easy to read letters. I do not want cursive (handwriting) letters. I thought about having a "reflection" of letters (mirror image), but think that this will be hard to read from far away. Maybe you can surprise me and come up with an idea that works using the a mirror image....but I'm not sure. I was leaning toward plain old BLOCK letters as I think it would be easy to read on my truck.

I would like to have 5 pages on my website:
1) Home
2) About Us (Know Your Poolman) / Why Hire Us
3) Services Offered
4) FAQ's
5) Contact

I am looking for a fully-functioning website (coded). Upon selection of the design winner, I am offering to increase the budget/payment by $100-$125 for the coding of all the pages. So anyone looking at participating in this contest, should be willing and able to provide the coding to the webpages that i've requested.

Target Market(s)

Upper middle-class homeowners who have a pool

Industry/Entity Type

Pool Service

Number of Pages Required

5+ page

Font styles to use
Serif

Colors
0455a3
3276b5
85acd3
85cae6
ffffff
33a6d7
0592cd

Requirements
Must have
• The Home page must have this picture highlighted in the top of the page:
• http://www.mesawaterpro.example/
• Must have pictures of some high-end pools. Any that you can find on the internet are wonderful.
• Must have a table on the right of the home page that mentions the service areas that we go to:
• • Carmel Valley (92130)
• • Del Mar (92014)
• • Rancho Santa Fe (92067)
• • Solana Beach (92075)
• • Santaluz (92127)
• • Cardiff (92007)
• • Encinitas (92024)
• • Carlsbad (92009, 92008)
• • La Jolla (92037)
• • Pacific Beach (92109)
• • Mira Mesa (92126)
• • Sorrento Valley (92121)
• • Clairemont (92117)
• • Rancho Bernardo (92127, 92128)
• • Rancho Penasquitos (92129)
• • Poway (92064)
• •
Nice to have
• Maybe incorporate some pictures of some kids (or families) playing in pools on the Why Hire Us page?
• I also like the feel of this website, but posting this page just for reference so you can get a feel more of what I like:
• http://www.crestlinepool.example/
• I like the FAQ's page from this website. I like how you can click on the question and then it pops up with the answer. http://www.dunewoodpoolcare.example/pool-spa-fountain-faqs/

```html
<!DOCTYPE html>
<html lang="en">
<head>
<meta charset="utf-8">
<title>FAQs – Glimmerwave Pool Service</title>
<link href="https://fonts.googleapis.com/css2?family=Tinos:ital,wght@0,400;0,700;1,400&family=Arimo:wght@700&display=swap" rel="stylesheet">
<style>
  :root {
    --water-deep: #0592cd;
    --water-mid: #33a6d7;
    --water-light: #85cae6;
    --brand-blue: #0455a3;
    --tagline-blue: #3276b5;
    --nav-top: #5aaea6;
    --nav-bottom: #3d8d88;
    --nav-active: #eef3c4;
    --panel: #ffffff;
    --heading: #3f6d69;
    --question: #111111;
    --answer: #555555;
    --footer-bar: #a79d93;
    --footer-link: #4a3c30;
    --footer-active: #fbf6ee;
  }
  * { box-sizing: border-box; margin: 0; padding: 0; }
  html, body { width: 767px; height: 1200px; overflow: hidden; }
  body { position: relative; font-family: "Tinos", "Times New Roman", serif; }

  .water-backdrop {
    position: absolute; inset: 0;
    background:
      radial-gradient(ellipse at 20% 30%, rgba(255,255,255,.35), transparent 45%),
      radial-gradient(ellipse at 80% 60%, rgba(255,255,255,.3), transparent 40%),
      radial-gradient(ellipse at 40% 85%, rgba(255,255,255,.25), transparent 40%),
      linear-gradient(160deg, var(--water-mid), var(--water-deep) 45%, var(--water-light) 75%, var(--water-mid));
  }

  .brand { position: absolute; left: 89px; top: 22px; display: flex; align-items: center; gap: 8px; }
  .brand-dot { width: 14px; height: 14px; border-radius: 50%; background: var(--brand-blue); }
  .brand-name { font-weight: 700; font-size: 17px; color: var(--brand-blue); letter-spacing: .3px; }
  .tagline {
    position: absolute; left: 244px; top: 36px;
    font-size: 19px; color: var(--brand-blue);
  }

  .main-nav {
    position: absolute; left: 84px; top: 112px; width: 617px; height: 35px;
    background: linear-gradient(var(--nav-top), var(--nav-bottom));
    border-top: 2px solid #79c2ba;
  }
  .main-nav a {
    position: absolute; top: 10px; transform: translateX(-50%);
    font-family: "Arimo", Arial, sans-serif; font-weight: 700; font-size: 11px;
    color: #fff; text-decoration: none; white-space: nowrap;
  }
  .main-nav a.is-current { color: var(--nav-active); }

  .content-panel {
    position: absolute; left: 84px; top: 163px; width: 616px; height: 974px;
    background: var(--panel);
    padding: 22px 28px 0 28px;
  }
  .page-title { font-weight: 400; font-size: 23px; line-height: 28px; color: var(--heading); }
  .section-title { font-weight: 400; font-size: 15px; line-height: 24px; color: var(--heading); }

  .faq-list { list-style: none; padding-left: 7px; }
  .faq-list li { height: 23.6px; }
  .faq-list summary {
    font-size: 11.5px; line-height: 23.6px; color: var(--question); cursor: pointer;
    list-style: none;
  }
  .faq-list summary::before { content: "\25B6"; font-size: 9px; margin-right: 6px; }

  .faq-open { margin-top: 13px; padding-left: 7px; }
  .faq-open summary {
    font-size: 11.5px; line-height: 14px; height: 16px; color: var(--question);
    border: 1px solid #8fb2d6; list-style: none; padding-left: 0;
  }
  .faq-open summary::before { content: "\25BC"; font-size: 9px; margin-right: 4px; }
  .faq-open p { font-size: 11px; line-height: 21px; color: var(--answer); padding-left: 1px; padding-right: 20px; }

  .list-general-top { margin-top: 20px; }
  .title-license { margin-top: 10px; }
  .list-license { margin-top: 6px; }
  .title-general { margin-top: 9px; }
  .list-general { margin-top: 7px; }

  .footer-nav {
    position: absolute; left: 84px; top: 1162px; width: 617px; height: 34px;
    background: var(--footer-bar);
    display: flex; align-items: center; gap: 13px; padding-left: 14px;
  }
  .footer-nav a { font-size: 11px; color: var(--footer-link); text-decoration: none; }
  .footer-nav a.is-current { color: var(--footer-active); }
</style>
</head>
<body>
  <div class="water-backdrop" role="img" aria-label="Rippling clear blue pool water background"></div>

  <header>
    <div class="brand"><span class="brand-dot"></span><span class="brand-name">Glimmerwave Pool Service</span></div>
    <p class="tagline">Water so pure, it sparkles like a summer sky.</p>
  </header>

  <nav class="main-nav">
    <a class="is-current" href="#" style="left:45px">HOME</a>
    <a href="#" style="left:132px">ABOUT US</a>
    <a href="#" style="left:221px">SERVICES</a>
    <a href="#" style="left:308px">FAQS</a>
    <a href="#" style="left:396px">WHY HIRE US</a>
    <a href="#" style="left:485px">CONTACT</a>
  </nav>

  <main class="content-panel">
    <h1 class="page-title">FAQS</h1>

    <details class="faq-open" open>
      <summary>What do you charge?</summary>
      <p>Because each pool is different, we do not have 1-size-fits-all pricing. Please call us at 858-555-0142 to make an appointment for a free assessment. We’ll come to your home or facility, discuss your specific needs, and provide a free customized pool service proposal for you.</p>
    </details>

    <ul class="faq-list list-general-top">
      <li><details><summary>Do you offer online bill pay?</summary></details></li>
      <li><details><summary>Automatic bill pay?</summary></details></li>
      <li><details><summary>Do you accept credit cards?</summary></details></li>
      <li><details><summary>How often do you show up?</summary></details></li>
      <li><details><summary>Do you ever show up unannounced?</summary></details></li>
      <li><details><summary>What happens if my regular technician calls in sick on my service day?</summary></details></li>
      <li><details><summary>What is included in your Weekly Full Service Program?</summary></details></li>
      <li><details><summary>What if there’s a problem with my equipment?</summary></details></li>
      <li><details><summary>If my pool needs water, will you add it during your weekly service call?</summary></details></li>
      <li><details><summary>What geographic areas do you serve?</summary></details></li>
    </ul>

    <h2 class="section-title title-license">Questions About License, Training and Insurance</h2>
    <ul class="faq-list list-license">
      <li><details><summary>Are your pool care technicians trained?</summary></details></li>
      <li><details><summary>Should my pool company be licensed?</summary></details></li>
      <li><details><summary>Why should a pool service company carry Liability Insurance?</summary></details></li>
      <li><details><summary>Why should my pool care technician be certified?</summary></details></li>
    </ul>

    <h2 class="section-title title-general">General FAQs</h2>
    <ul class="faq-list list-general">
      <li><details><summary>How can I tell if my pool is leaking?</summary></details></li>
      <li><details><summary>How do I determine how many gallons of water there are in my pool?</summary></details></li>
      <li><details><summary>How often does my pool filter need to be cleaned?</summary></details></li>
      <li><details><summary>Why do my pool and spa need to be chlorinated?</summary></details></li>
      <li><details><summary>Do you service salt pools?</summary></details></li>
      <li><details><summary>Is a salt chlorinated system better than the traditional hand chlorinated system?</summary></details></li>
      <li><details><summary>How often should I change the water in my pool?</summary></details></li>
      <li><details><summary>What is TDS?</summary></details></li>
      <li><details><summary>Should I change my own water?</summary></details></li>
      <li><details><summary>How often do I need an acid wash?</summary></details></li>
      <li><details><summary>My hair turns green when I swim, is this caused by the chlorine?</summary></details></li>
      <li><details><summary>Why should I use a pool service?</summary></details></li>
      <li><details><summary>If I have a pool service do I still need to empty my baskets?</summary></details></li>
      <li><details><summary>Is it ok to drain my pool for the winter?</summary></details></li>
      <li><details><summary>How long does it take to heat my spa with a gas heater?</summary></details></li>
      <li><details><summary>How long does it take to heat my spa with an electric heater?</summary></details></li>
      <li><details><summary>What cities do you offer weekly pool cleaning?</summary></details></li>
    </ul>
  </main>

  <footer class="footer-nav">
    <a class="is-current" href="#">HOME</a>
    <a href="#">ABOUT US</a>
    <a href="#">SERVICES</a>
    <a href="#">FAQS</a>
    <a href="#">WHY HIRE US</a>
    <a href="#">CONTACT</a>
  </footer>
</body>
</html>
```